Etiketten für Herstellung von Tahini und Helva
Zielgruppe
Verarbeitung Sesam
Herstellung Helva
Beispiel habe ich beigefügt
ANBEI FINDEN SIE NEUES BILD ' IN DIESER RICHTUNG '
Aufgabenstellung
Label Durchmesser ca 12 cm ( Verpackung ist PP Schale durchsichtig) Verpackung bild finden Sie anbei
oben kommt Marke + Bild
unten die Inhaltstoffe usw.
Made in Germany ,
100% Natur
Helva mit Vanillegeschmack, with vanilla aroma, vanilya Aromali
Süße Sesampaste
Traditional türkische Spezialität
Bitte nur Helva als Produktname eintragen

```html
<!DOCTYPE html>
<html lang="de">
<head>
<meta charset="utf-8">
<title>Helva Etiketten</title>
<link rel="stylesheet" href="https://fonts.googleapis.com/css2?family=Tenor+Sans&family=Pathway+Gothic+One&display=swap">
<style>
  :root {
    --canvas: #ffffff;
    --label-dark: #1e1e1c;
    --gold: #d9ae5f;
    --band-gold: #dfb567;
    --brand-green: #3f8f3a;
    --ring-pistachio: #a8c90f;
    --ring-honey: #f7c900;
    --ring-vanilla: #7a4a2c;
    --badge-cream: #f0e2c4;
  }
  html, body {
    margin: 0;
    padding: 0;
    width: 1200px;
    height: 478px;
    overflow: hidden;
    background: var(--canvas);
  }
  .label-row {
    position: relative;
    width: 1200px;
    height: 478px;
  }
  .label {
    position: absolute;
    width: 384px;
    height: 384px;
  }
  .label--pistachio { left: 21px; top: 23px; }
  .label--honey { left: 411px; top: 20px; }
  .label--vanilla { left: 796px; top: 23px; }
  .label .face { fill: var(--label-dark); }
  .label .band { fill: var(--band-gold); }
  .label .band-edge { stroke: var(--label-dark); stroke-width: 1; fill: none; }
  .label--pistachio .ring { stroke: var(--ring-pistachio); }
  .label--honey .ring { stroke: var(--ring-honey); }
  .label--vanilla .ring { stroke: var(--ring-vanilla); }
  .ring { fill: none; stroke-width: 4; }
  .brand-name {
    font-family: "Tenor Sans", sans-serif;
    font-size: 16px;
    letter-spacing: 1px;
    fill: var(--brand-green);
  }
  .product-name {
    font-family: "Tenor Sans", sans-serif;
    font-size: 82px;
    fill: var(--gold);
  }
  .descriptor {
    font-family: "Pathway Gothic One", sans-serif;
    font-size: 15px;
    fill: var(--gold);
  }
  .badge--light { fill: var(--badge-cream); stroke: var(--label-dark); stroke-width: 1.5; }
  .badge--dark { fill: var(--label-dark); stroke: var(--badge-cream); stroke-width: 2; }
</style>
</head>
<body>
<div class="label-row">

  <svg class="label label--pistachio" viewBox="0 0 384 384" aria-label="Helva mit Pistazien">
    <defs>
      <clipPath id="clip-pistachio"><circle cx="192" cy="192" r="184"/></clipPath>
      <linearGradient id="halva-pistachio" x1="0" y1="0" x2="1" y2="1">
        <stop offset="0" stop-color="#ead5a6"/>
        <stop offset="0.7" stop-color="#d7b783"/>
        <stop offset="1" stop-color="#8fb04a"/>
      </linearGradient>
    </defs>
    <g clip-path="url(#clip-pistachio)">
      <rect class="face" x="0" y="0" width="384" height="384"/>
      <rect class="band" x="0" y="258" width="384" height="126"/>
      <circle class="band-edge" cx="192" cy="192" r="181"/>
      <path role="img" aria-label="Foto: Helvastücke mit Pistazien" fill="url(#halva-pistachio)"
        d="M160 232 L196 224 L200 200 L228 168 L262 172 L360 240 L345 282 L300 306 L250 308 L200 300 L162 290 Z"/>
    </g>
    <circle class="ring" cx="192" cy="192" r="186"/>
    <text class="brand-name" x="192" y="95" text-anchor="middle">MONDKORN</text>
    <text class="product-name" x="194" y="163" text-anchor="middle" textLength="248" lengthAdjust="spacingAndGlyphs">HELVA</text>
    <text class="descriptor" x="161" y="182" text-anchor="middle" textLength="80" lengthAdjust="spacingAndGlyphs">Süße Sesampaste</text>
    <text class="descriptor" x="113" y="205" text-anchor="middle" textLength="154" lengthAdjust="spacingAndGlyphs">Traditionelle türkische Spezialität</text>
    <text class="descriptor" x="119" y="220" text-anchor="middle" textLength="127" lengthAdjust="spacingAndGlyphs">mit Pistazien - with pistacio</text>
    <text class="descriptor" x="126" y="236" text-anchor="middle" textLength="53" lengthAdjust="spacingAndGlyphs">Antep figist</text>
    <circle class="badge--light" cx="133" cy="322" r="24"/>
    <circle class="badge--light" cx="191" cy="322" r="24"/>
    <circle class="badge--dark" cx="251" cy="324" r="24"/>
  </svg>

  <svg class="label label--honey" viewBox="0 0 384 384" aria-label="Helva mit Honig">
    <defs>
      <clipPath id="clip-honey"><circle cx="192" cy="192" r="184"/></clipPath>
      <linearGradient id="halva-honey" x1="0" y1="0" x2="1" y2="1">
        <stop offset="0" stop-color="#ead5a6"/>
        <stop offset="0.6" stop-color="#d7b783"/>
        <stop offset="1" stop-color="#f0a020"/>
      </linearGradient>
    </defs>
    <g clip-path="url(#clip-honey)">
      <rect class="face" x="0" y="0" width="384" height="384"/>
      <rect class="band" x="0" y="258" width="384" height="126"/>
      <circle class="band-edge" cx="192" cy="192" r="181"/>
      <path role="img" aria-label="Foto: Helvastücke mit Honigwabe und Honiglöffel" fill="url(#halva-honey)"
        d="M156 232 L194 222 L198 200 L226 166 L260 170 L352 238 L338 282 L300 306 L250 310 L200 304 L158 290 Z"/>
    </g>
    <circle class="ring" cx="192" cy="192" r="186"/>
    <text class="brand-name" x="192" y="95" text-anchor="middle">MONDKORN</text>
    <text class="product-name" x="194" y="163" text-anchor="middle" textLength="248" lengthAdjust="spacingAndGlyphs">HELVA</text>
    <text class="descriptor" x="160" y="182" text-anchor="middle" textLength="80" lengthAdjust="spacingAndGlyphs">Süße Sesampaste</text>
    <text class="descriptor" x="112" y="205" text-anchor="middle" textLength="154" lengthAdjust="spacingAndGlyphs">Traditionelle türkische Spezialität</text>
    <text class="descriptor" x="128" y="220" text-anchor="middle" textLength="109" lengthAdjust="spacingAndGlyphs">mit Honig  - with honey</text>
    <text class="descriptor" x="138" y="236" text-anchor="middle" textLength="28" lengthAdjust="spacingAndGlyphs">bal ile</text>
    <circle class="badge--light" cx="133" cy="322" r="24"/>
    <circle class="badge--light" cx="191" cy="322" r="24"/>
    <circle class="badge--dark" cx="251" cy="324" r="24"/>
  </svg>

  <svg class="label label--vanilla" viewBox="0 0 384 384" aria-label="Helva mit Vanillegeschmack">
    <defs>
      <clipPath id="clip-vanilla"><circle cx="192" cy="192" r="184"/></clipPath>
      <linearGradient id="halva-vanilla" x1="0" y1="0" x2="1" y2="1">
        <stop offset="0" stop-color="#ead5a6"/>
        <stop offset="0.6" stop-color="#d7b783"/>
        <stop offset="1" stop-color="#f2d640"/>
      </linearGradient>
    </defs>
    <g clip-path="url(#clip-vanilla)">
      <rect class="face" x="0" y="0" width="384" height="384"/>
      <rect class="band" x="0" y="258" width="384" height="126"/>
      <circle class="band-edge" cx="192" cy="192" r="181"/>
      <path role="img" aria-label="Foto: Helvastücke mit Vanilleschoten und Vanilleblüte" fill="url(#halva-vanilla)"
        d="M160 234 L186 226 L190 202 L222 170 L256 174 L358 240 L344 282 L300 306 L250 310 L200 304 L162 292 Z"/>
    </g>
    <circle class="ring" cx="192" cy="192" r="186"/>
    <text class="brand-name" x="192" y="95" text-anchor="middle">MONDKORN</text>
    <text class="product-name" x="194" y="163" text-anchor="middle" textLength="248" lengthAdjust="spacingAndGlyphs">HELVA</text>
    <text class="descriptor" x="160" y="182" text-anchor="middle" textLength="80" lengthAdjust="spacingAndGlyphs">Süße Sesampaste</text>
    <text class="descriptor" x="103" y="205" text-anchor="middle" textLength="154" lengthAdjust="spacingAndGlyphs">Traditionelle türkische Spezialität</text>
    <text class="descriptor" x="125" y="220" text-anchor="middle" textLength="98" lengthAdjust="spacingAndGlyphs">mit Vanillegeschmack</text>
    <text class="descriptor" x="105" y="236" text-anchor="middle" textLength="86" lengthAdjust="spacingAndGlyphs">with vanilla aroma</text>
    <text class="descriptor" x="108" y="251" text-anchor="middle" textLength="72" lengthAdjust="spacingAndGlyphs">Vanilva Aromali</text>
    <circle class="badge--light" cx="133" cy="322" r="24"/>
    <circle class="badge--light" cx="191" cy="322" r="24"/>
    <circle class="badge--dark" cx="251" cy="324" r="24"/>
  </svg>

</div>
</body>
</html>
```